4 page website for our new business,
www.Velna Crest Bathrooms.example
We will provide the follwing service
1st Home page, bathroom renvovations, make over redesign etc
2nd page Tiling service
3rd page Waterproofing
4th page Galllery
The home will maily focus on the core business bathroom renovation, customer should able request quote, via entering thier info eg. name and contact number and select the 3 services
Need area for testimonials that will scroll
Maybe a banner which may flash varies pic of different design
Maybe a area for giving reasons why customer should go with us for they job
simple site which will grentrate leads, create presece, build brand.
We've just had the logo design, which allow you to create theme.
Target Market(s)
home owner's mum and dad
Look and feel
Each slider illustrates characteristics of the customer's brand and the style your logo design should communicate.

```html
<!DOCTYPE html>
<html lang="en">
<head>
<meta charset="utf-8">
<title>Velna Crest Bathroom</title>
<link href="https://fonts.googleapis.com/css2?family=Arimo:wght@400;700&family=Open+Sans:wght@400;600&family=Roboto+Condensed:wght@400;700&display=swap" rel="stylesheet">
<style>
:root{
  --page-bg:#e9e9e9;
  --panel-fade:#f6f6f6;
  --ink:#1c1c1c;
  --body-text:#8c8c8c;
  --dark-text:#444;
  --accent:#3a8fd9;
  --accent-bright:#1a9be6;
  --orange:#f3a21e;
  --rule:#d6d6d6;
  --footer:#474747;
  --footer-line:#6a6a6a;
  --footer-text:#d8d8d8;
  --tick:#3aa12a;
}
*{box-sizing:border-box;margin:0;padding:0}
html,body{width:1200px;height:2211px;overflow:hidden}
body{background:var(--page-bg);font-family:"Arimo",Arial,sans-serif;color:var(--body-text);position:relative}
.site{position:absolute;left:124px;top:96px;width:952px;height:2015px;background:linear-gradient(#fff,var(--panel-fade) 60%,#fff);border-radius:6px 6px 0 0;box-shadow:0 0 6px rgba(0,0,0,.08)}
.abs{position:absolute}
.search{left:709px;top:13px;width:206px;height:22px;border:1px solid #cfcfcf;border-radius:11px;background:#fafafa;font-size:11px;color:#b5b5b5;padding:4px 12px}
.search-btn{position:absolute;right:-1px;top:-1px;width:22px;height:22px;border-radius:50%;border:1px solid #cfcfcf;background:#eee}
.logo{left:56px;top:60px;display:flex;align-items:center;gap:9px;font-family:"Open Sans",sans-serif;font-size:24px;font-weight:400;color:#333;letter-spacing:-.5px;white-space:nowrap}
.logo-dot{width:14px;height:14px;border-radius:50%;background:var(--orange)}
.nav{right:37px;top:73px;display:flex;gap:9px;white-space:nowrap}
.nav a{font-size:11px;line-height:14px;color:#333;text-decoration:none;border:1px solid #c4c4c4;border-radius:11px;padding:4px 9px;background:linear-gradient(#fff,#eaeaea);white-space:nowrap}
.nav a.current{background:#3d3d3d;color:#fff;border-color:#3d3d3d}
.slider{left:35px;top:137px;width:882px;height:391px;border-radius:8px;background:linear-gradient(100deg,#4a4a48 0%,#8a8986 35%,#d9dadb 60%,#b9b9b7 100%)}
.arrow{top:304px;width:22px;height:50px;background:#8f8f8f;border:2px solid #ddd}
.arrow.prev{left:0;border-radius:0 25px 25px 0}
.arrow.next{right:0;border-radius:25px 0 0 25px}
.arrow svg{position:absolute;top:16px}
.caption{left:54px;top:299px;width:425px;height:192px;background:rgba(255,255,255,.78);padding:24px 26px}
.caption h2{font-family:"Roboto Condensed",sans-serif;font-size:18px;color:#222;text-transform:uppercase;border-bottom:1px solid #bbb;padding-bottom:6px;margin-bottom:16px}
.caption p{font-size:11px;line-height:17px;color:#555}
.caption strong{color:var(--accent-bright)}
.dots{left:452px;top:543px;display:flex;gap:3px}
.dots i{width:9px;height:9px;border-radius:50%;background:#666}
.dots i.on{background:var(--accent-bright)}
.divider{left:68px;width:815px;height:1px;background:var(--rule);box-shadow:0 6px 10px rgba(0,0,0,.05)}
h3.title{font-family:"Roboto Condensed",sans-serif;font-weight:700;font-size:22px;color:var(--ink)}
.sub{font-family:"Roboto Condensed",sans-serif;font-size:17px;color:var(--accent)}
.copy{font-size:11.5px;line-height:17px;color:var(--body-text)}
.copy strong{color:var(--dark-text)}
.btn{font-size:12px;color:#333;border:1px solid #bdbdbd;border-radius:12px;padding:3px 10px;background:linear-gradient(#fff,#e9e9e9);display:inline-flex;align-items:center;gap:6px;white-space:nowrap}
.photo{border-radius:6px}
.card h4{font-family:"Roboto Condensed",sans-serif;font-size:17px;color:var(--ink);margin-bottom:8px}
.checks{list-style:none}
.checks li{font-size:11.5px;height:28px;display:flex;align-items:center;gap:10px;padding-left:8px}
.quote-form{left:41px;top:1640px;width:270px;display:grid;grid-template-columns:1fr 1fr;gap:6px}
.quote-form .field{height:24px;border:1px solid #cfcfcf;border-radius:4px;background:#fff;font-size:11px;color:#aaa;padding:5px 8px;white-space:nowrap;overflow:hidden}
.quote-form .wide{grid-column:1 / 3}
.quote-form .select{display:flex;justify-content:space-between;align-items:center}
.quote-form .btn{justify-self:start}
.quote{width:280px;background:#ececec;border-radius:6px;padding:8px 10px;font-size:11.5px;line-height:17px;font-style:italic;color:#777}
.quote::after{content:"";position:absolute;right:60px;bottom:-10px;border:10px solid transparent;border-top-color:#ececec;border-bottom:0}
.author{font-size:12px;color:#444;width:280px;text-align:right;padding-right:14px}
.thumb{width:81px;height:86px;border:3px solid #fff;box-shadow:0 0 3px rgba(0,0,0,.3)}
.project{font-size:11px;line-height:14px;color:#333}
.project h5{font-size:13px;font-weight:400;color:var(--accent-bright);margin-bottom:12px}
.project a{color:var(--accent-bright)}
.dash{left:638px;width:262px;border-top:1px dashed #bdbdbd}
.footer{left:0;top:1757px;width:952px;height:258px;background:var(--footer);border-radius:0 0 6px 6px}
.fcol{top:28px;width:200px}
.fcol h6{font-family:"Roboto Condensed",sans-serif;font-weight:400;font-size:16px;color:#fff;margin-bottom:14px}
.fcol li{list-style:none;font-size:11px;color:var(--footer-text);height:34px;line-height:34px;padding-left:10px;border-bottom:1px dotted var(--footer-line);white-space:nowrap}
.fcol li.big{font-size:15px;color:#fff}
.social{left:570px;top:2126px;display:flex;gap:6px}
.social i{width:18px;height:18px;background:#4b4b4b;border-radius:2px}
.copyright{left:0;width:1200px;top:2162px;text-align:center;font-size:11px;color:#777}
</style>
</head>
<body>
<div class="site">
  <div class="abs search">search...<span class="search-btn"></span></div>
  <div class="abs logo"><span class="logo-dot"></span>Velna Crest Bathroom</div>
  <nav class="abs nav">
    <a class="current" href="#">Home</a><a href="#">Renovation</a><a href="#">Tiling service</a><a href="#">Waterproofing</a><a href="#">Gallery</a><a href="#">Contact</a>
  </nav>

  <div class="abs slider" role="img" aria-label="Photo of a modern bathroom with a freestanding bathtub by a large window"></div>
  <div class="abs arrow prev"><svg width="12" height="14" style="left:4px"><path d="M9 1 L2 7 L9 13Z" fill="#fff"/></svg></div>
  <div class="abs arrow next"><svg width="12" height="14" style="left:6px"><path d="M3 1 L10 7 L3 13Z" fill="#fff"/></svg></div>
  <div class="abs caption">
    <h2>A new way to make over your bathroom</h2>
    <p><strong>Duis autem vel eum iriure dolor in hendrerit in vulputate velit esse molestie consequat, vel illum dolore eu feugiat.</strong> nulla facilisis at vero eros et accumsan et iusto odio dignissim qui blandit praesent luptatum zzril delenit augue duis dolore te feugait nulla facilisi. Lorem ipsum dolor sit amet, consectetuer adipiscing elit, sed diam nonummy nibh euismod tincidunt ut laoreet dolore magna aliquam erat volutpat.</p>
  </div>
  <div class="abs dots"><i class="on"></i><i></i><i></i><i></i><i></i><i></i></div>

  <div class="abs divider" style="top:578px"></div>

  <section class="abs" style="left:41px;top:624px;width:490px">
    <h3 class="title">Welcome to Our Company</h3>
    <div class="sub">A new way to make over your bathroom</div>
    <p class="copy" style="margin-top:14px"><strong>Duis autem vel eum iriure dolor in hendrerit in vulputate velit esse molestie consequat, vel illum dolore eu feugiat.</strong> nulla facilisis at vero eros et accumsan et iusto odio dignissim qui blandit praesent luptatum zzril delenit augue duis dolore te feugait nulla facilisi. Lorem ipsum dolor sit amet, consectetuer adipiscing elit, sed diam nonummy nibh euismod tincidunt ut laoreet dolore magna aliquam erat volutpat.</p>
  </section>
  <div class="abs btn" style="left:455px;top:780px">Read more <svg width="10" height="8"><path d="M0 2h5V0l5 4-5 4V6H0z" fill="var(--accent-bright)"/></svg></div>
  <div class="abs photo" style="left:562px;top:626px;width:335px;height:177px;background:linear-gradient(90deg,#4d4f49,#5f7a45 50%,#8f9188)" role="img" aria-label="Photo of a bathroom with a green plant wall and freestanding tub"></div>

  <div class="abs divider" style="top:852px"></div>

  <div class="abs photo" style="left:35px;top:908px;width:282px;height:134px;background:linear-gradient(90deg,#6f7a1e,#b8c53a,#5d5f2a)" role="img" aria-label="Photo of a lime green designed bathroom"></div>
  <div class="abs photo" style="left:336px;top:908px;width:282px;height:134px;background:linear-gradient(90deg,#8d6a44,#c9a67a,#7d5a36)" role="img" aria-label="Photo of a bathroom under renovation with timber framing"></div>
  <div class="abs photo" style="left:637px;top:908px;width:282px;height:134px;background:linear-gradient(#e7e7ea,#6c5d8a 55%,#9a9aa4)" role="img" aria-label="Photo of a made over bathroom with purple walls and clawfoot tub"></div>

  <div class="abs card" style="left:35px;top:1068px;width:282px">
    <h4>Design Services</h4>
    <p class="copy">Duis autem vel eum iriure dolor in hendrerit in vulputate velit esse molestie consequat, vel illum dolore eu feugiat. nulla facilisis at vero eros et accumsan.</p>
  </div>
  <div class="abs card" style="left:336px;top:1068px;width:282px">
    <h4>Renovation</h4>
    <p class="copy">Duis autem vel eum iriure dolor in hendrerit in vulputate velit esse molestie consequat, vel illum dolore eu feugiat. nulla facilisis at vero eros et accumsan.</p>
  </div>
  <div class="abs card" style="left:637px;top:1068px;width:282px">
    <h4>Make Over</h4>
    <p class="copy">Duis autem vel eum iriure dolor in hendrerit in vulputate velit esse molestie consequat, vel illum dolore eu feugiat. nulla facilisis at vero eros et accumsan.</p>
  </div>
  <div class="abs btn" style="left:226px;top:1160px">Read more <svg width="10" height="8"><path d="M0 2h5V0l5 4-5 4V6H0z" fill="var(--accent-bright)"/></svg></div>
  <div class="abs btn" style="left:527px;top:1160px">Read more <svg width="10" height="8"><path d="M0 2h5V0l5 4-5 4V6H0z" fill="var(--accent-bright)"/></svg></div>
  <div class="abs btn" style="left:828px;top:1160px">Read more <svg width="10" height="8"><path d="M0 2h5V0l5 4-5 4V6H0z" fill="var(--accent-bright)"/></svg></div>

  <div class="abs divider" style="top:1226px"></div>

  <section class="abs" style="left:41px;top:1262px;width:280px">
    <h3 class="title">What We Do?</h3>
    <div class="sub">We can serve your Bathroom</div>
    <p class="copy" style="margin-top:14px">Ut wisi enim ad minim veniam, quis nostrud exerci tation ullamcorper suscipit lobortis nisl ut aliquip ex ea commodo consequat.</p>
    <ul class="checks" style="margin-top:14px">
      <li><svg width="12" height="10"><path d="M1 5l3 3 7-7" stroke="var(--tick)" stroke-width="2.5" fill="none"/></svg>Nam liber tempor cum soluta.</li>
      <li><svg width="12" height="10"><path d="M1 5l3 3 7-7" stroke="var(--tick)" stroke-width="2.5" fill="none"/></svg>Nobis eleifend option congue nihil.</li>
      <li><svg width="12" height="10"><path d="M1 5l3 3 7-7" stroke="var(--tick)" stroke-width="2.5" fill="none"/></svg>Doming id quod mazim.</li>
      <li><svg width="12" height="10"><path d="M1 5l3 3 7-7" stroke="var(--tick)" stroke-width="2.5" fill="none"/></svg>Lorem ipsum dolor sit amet.</li>
      <li><svg width="12" height="10"><path d="M1 5l3 3 7-7" stroke="var(--tick)" stroke-width="2.5" fill="none"/></svg>Adipiscing elit, sed diam nonummy nibh.</li>
      <li><svg width="12" height="10"><path d="M1 5l3 3 7-7" stroke="var(--tick)" stroke-width="2.5" fill="none"/></svg>Erat volutpat. Ut wisi enim ad minim.</li>
      <li><svg width="12" height="10"><path d="M1 5l3 3 7-7" stroke="var(--tick)" stroke-width="2.5" fill="none"/></svg>Quis nostrud exerci tation ullamcorper.</li>
      <li><svg width="12" height="10"><path d="M1 5l3 3 7-7" stroke="var(--tick)" stroke-width="2.5" fill="none"/></svg>Lobortis nisl ut aliquip ex ea commodo.</li>
    </ul>
  </section>

  <form class="abs quote-form" aria-label="Request a quote">
    <div class="field">Your name</div>
    <div class="field">Contact number</div>
    <div class="field wide select">Select service: Renovation / Tiling / Waterproofing <svg width="8" height="5"><path d="M0 0h8L4 5z" fill="#888"/></svg></div>
    <div class="btn">Request a quote <svg width="10" height="8"><path d="M0 2h5V0l5 4-5 4V6H0z" fill="var(--accent-bright)"/></svg></div>
  </form>

  <section class="abs" style="left:343px;top:1262px;width:280px">
    <h3 class="title">What They Say</h3>
    <div class="sub">Testimonial our client</div>
  </section>
  <blockquote class="abs quote" style="left:336px;top:1325px;height:94px">"Duis autem vel eum iriure dolor in hendrerit in vulputate velit esse molestie consequat, vel illum dolore eu feugiat nulla facilisis. At vero eos et accumsan et justo duo dolores et ea rebum. Stet clita kasd gubergren."</blockquote>
  <div class="abs author" style="left:336px;top:1430px">- Dana Morrow -</div>
  <blockquote class="abs quote" style="left:336px;top:1459px;height:77px">"Duis autem vel eum iriure dolor in hendrerit in vulputate velit esse molestie consequat, vel illum dolore eu feugiat nulla facilisis. At vero eos et accumsan et justo duo dolores et ea rebum."</blockquote>
  <div class="abs author" style="left:336px;top:1548px">- Dana Morrow -</div>
  <blockquote class="abs quote" style="left:336px;top:1577px;height:60px">"Duis autem vel eum iriure dolor in hendrerit in vulputate velit esse molestie consequat, vel illum dolore eu feugiat nulla facilisis."</blockquote>
  <div class="abs author" style="left:336px;top:1650px">- Dana Morrow -</div>
  <div class="abs btn" style="left:534px;top:1706px">Read more <svg width="10" height="8"><path d="M0 2h5V0l5 4-5 4V6H0z" fill="var(--accent-bright)"/></svg></div>

  <section class="abs" style="left:638px;top:1262px;width:280px">
    <h3 class="title">Our Recent WorkS</h3>
    <div class="sub">Portfolio Gallery</div>
  </section>
  <div class="abs thumb" style="left:638px;top:1326px;background:linear-gradient(#cfd3d6,#7c8388)" role="img" aria-label="Photo of a hotel bathroom project"></div>
  <div class="abs project" style="left:734px;top:1328px">
    <h5>PROJECT 1</h5>
    <p>New Design for Hotel.</p><p style="margin-top:12px">Location : London, England.</p><p>Author : <a>Marlo Tennant</a></p>
  </div>
  <div class="abs dash" style="top:1424px"></div>
  <div class="abs thumb" style="left:638px;top:1438px;background:linear-gradient(#e4e4e8,#6c5d8a)" role="img" aria-label="Photo of a bathroom make over project"></div>
  <div class="abs project" style="left:734px;top:1440px">
    <h5>PROJECT 2</h5>
    <p>Bathroom Make over</p><p>Location : London, England.</p><p>Author : <a>Marlo Tennant</a></p>
  </div>
  <div class="abs dash" style="top:1540px"></div>
  <div class="abs thumb" style="left:638px;top:1555px;background:linear-gradient(90deg,#6f7a1e,#b8c53a)" role="img" aria-label="Photo of a painted and decorated bathroom project"></div>
  <div class="abs project" style="left:734px;top:1556px;width:170px">
    <h5>PROJECT 3</h5>
    <p>Home painting &amp; Decorating in Bathroom</p><p>Location : London, England.</p><p>Author : <a>Marlo Tennant</a></p>
  </div>
  <div class="abs btn" style="left:824px;top:1683px">More Project <svg width="10" height="8"><path d="M0 2h5V0l5 4-5 4V6H0z" fill="var(--accent-bright)"/></svg></div>

  <footer class="abs footer">
    <div class="abs fcol" style="left:38px"><h6>Site Map</h6><ul><li>Home</li><li>Renovation</li><li>Tilling Services</li><li>Waterproofing</li><li>Gallery</li></ul></div>
    <div class="abs fcol" style="left:262px"><h6>Our Company</h6><ul><li>About Us</li><li>Terms &amp; Condition</li><li>Privacy Police</li><li>Contact Us</li></ul></div>
    <div class="abs fcol" style="left:486px"><h6>Our Services</h6><ul><li>Design &amp; Consultant Project</li><li>Bathroom Renovations</li><li>Bathroom Make Over</li><li>Product &amp; Selling</li></ul></div>
    <div class="abs fcol" style="left:712px"><h6>Contact Us</h6><ul><li>14 Harlow Lane here</li><li>Sample City - Sample Country</li><li class="big">+000-555-0147</li><li class="big">info@velnacrest.example</li></ul></div>
  </footer>
</div>
<div class="abs social"><i></i><i></i><i></i></div>
<div class="abs copyright">VelnaCrestBathroom © 2012 - All Right Reserved</div>
</body>
</html>
```